Inspiring Fundraising Foundation Website to Provide Academic Scholarships

Hello, we are launching a foundation to provide academic scholarships to high school students for college. We'd like this to be an informational website with contact information. There will be a total of approximately 5-7 pages in all.
The color scheme will be purple and white, with a girly feel. I 've attached the logo for reference!

Target Market(s)

high school students, college students

Industry/Entity Type

Education

Coding

Coded - Design and coding required

Number of Pages Required

5+ page

Font styles to use
Serif
Sans Serif
Script

Colors
6b449b
886aae
b7a5cd
e4daeb
ffffff
fdf9cf
fbf289

Requirements
Must have
• Purple, girly feel, to reflect the logo's style. Should be light-themed
Should not have
• No dark themes (aka heavy on black or dark colors)

```html
<!DOCTYPE html>
<html lang="en">
<head>
<meta charset="utf-8">
<title>Lorena Valdez Foundation</title>
<link rel="stylesheet" href="https://fonts.googleapis.com/css2?family=Arimo:wght@400;700&family=Raleway:wght@300;400&display=swap">
<style>
:root{
  --purple:#4a2a86;
  --purple-mid:#6b449b;
  --lilac:#b7a5cd;
  --lilac-soft:#e4daeb;
  --white:#ffffff;
  --ink:#333333;
  --grey-text:#8a8a8a;
  --panel:#e6e6e6;
  --card:#f1f1f1;
  --footer:#464646;
  --caption:rgba(20,20,20,.72);
}
*{box-sizing:border-box;margin:0;padding:0}
html,body{width:1200px;height:2769px;overflow:hidden}
body{position:relative;background:var(--white);font-family:"Arimo",Arial,sans-serif;color:var(--ink)}
.abs{position:absolute}

.top-bar{left:0;top:0;width:1200px;height:34px;background:var(--purple)}
.top-links{right:114px;top:0;height:34px;display:flex;gap:18px;align-items:center;list-style:none}
.top-links li{color:var(--white);font-size:9.5px;font-weight:700;letter-spacing:.2px}

.brand{left:102px;top:70px;display:flex;align-items:center;gap:12px}
.brand-mark{width:26px;height:26px;border-radius:50%;background:var(--purple-mid)}
.brand-name{font-size:25px;font-weight:700;color:var(--purple);line-height:1.15}

.search{left:862px;top:114px;width:236px;height:28px;border-bottom:2px solid var(--lilac-soft);color:var(--lilac);font-size:15px;padding-left:2px}

.main-nav{left:102px;top:220px;width:996px;display:flex;justify-content:space-between;list-style:none}
.main-nav li{font-size:15px;font-weight:700;color:var(--purple);display:flex;align-items:center;gap:7px}
.caret{width:9px;height:6px}

.hero{left:0;top:264px;width:1200px;height:539px;background:linear-gradient(90deg,#6f5d4b 0%,#a38f75 35%,#8c7c6a 55%,#b6ad9f 80%,#8e8478 100%)}
.hero-title{left:103px;top:440px;font-family:"Raleway",Arial,sans-serif;font-weight:300;font-size:35px;line-height:40px;color:var(--white)}

.feature{top:873px;width:330px;height:246px}
.feature .photo{position:absolute;inset:0}
.feature .caption{position:absolute;left:0;bottom:0;width:100%;height:64px;background:var(--caption);padding:6px 8px;color:var(--white)}
.feature h3{font-size:17px;font-weight:700;margin-bottom:4px}
.feature p{font-size:10.5px;line-height:13px}

.intro-title{left:102px;top:1174px;width:960px;font-size:45px;line-height:50px;color:var(--purple);font-weight:400}
.intro-copy{left:102px;top:1306px;width:610px;font-size:14.5px;line-height:20.5px;color:var(--grey-text)}
.bullets{left:102px;top:1444px;list-style:none;font-size:14.5px;color:var(--grey-text)}
.bullets li{height:37px;display:flex;align-items:center;gap:6px}
.bullets li:nth-child(3){margin-top:3px}
.bullets .dot{width:7px;height:7px;border-radius:50%;background:var(--purple)}
.bullets b{color:var(--purple)}
.intro-photo{left:777px;top:1307px;width:321px;height:181px;background:linear-gradient(180deg,#c9b896 0%,#8f7b66 45%,#2c2a36 100%)}

.section-title{left:102px;top:1628px;font-size:31px;font-weight:700;color:var(--purple);letter-spacing:-.3px}

.program{top:1674px;width:319px;height:338px;background:var(--card)}
.program .photo{height:187px}
.program h4{margin:24px 12px 4px;font-size:16px;font-weight:400;color:var(--ink)}
.program p{margin:0 12px;font-size:12.5px;line-height:21px;color:var(--grey-text)}
.program .btn{position:absolute;left:0;bottom:0;width:100%;height:35px;background:var(--purple);color:var(--white);font-size:13.5px;display:flex;align-items:center;justify-content:center}

.apply{left:102px;top:2043px;width:996px;height:427px;background:var(--panel)}
.apply h2{position:absolute;top:18px;width:100%;text-align:center;font-size:33px;font-weight:400;color:var(--purple)}
.field{position:absolute;left:13px;width:970px}
.field label{display:block;font-size:13px;color:#555;margin-left:-3px}
.field label span{color:#c04040;margin-right:3px}
.field .input{margin-top:6px;height:42px;background:var(--white);border:1px solid #cfcfcf}
.signup{position:absolute;left:13px;top:373px;width:970px;height:37px;background:var(--purple);color:var(--white);font-size:17px;display:flex;align-items:center;justify-content:center}

.footer{left:0;top:2503px;width:1200px;height:266px;background:var(--footer)}
.footer-brand{left:102px;top:2620px;display:flex;align-items:center;gap:10px}
.footer-brand .brand-mark{background:var(--white);width:22px;height:22px}
.footer-brand .brand-name{color:var(--white);font-size:21px}
.footer-info{left:318px;top:2574px;color:var(--white);font-size:17.5px;line-height:32px}
.socials{left:787px;top:2697px;display:flex;gap:12px;list-style:none}
.socials li{width:41px;height:41px;border-radius:50%;border:2px solid var(--white)}
.socials li:nth-child(1){background:#2d7ab3}
.socials li:nth-child(2){background:#35a6e0}
.socials li:nth-child(3){background:#3a5b9e}
.socials li:nth-child(4){background:#b8418e}
.socials li:nth-child(5){background:#d6492f}
.socials li:nth-child(6){background:#d83a2c}
</style>
</head>
<body>
<header>
  <div class="abs top-bar"></div>
  <ul class="abs top-links">
    <li>SCHOOL OF COMMUNICATION</li><li>ABOUT</li><li>NEWS</li><li>SUPPORT</li><li>CONTACT</li>
  </ul>
  <div class="abs brand">
    <span class="brand-mark"></span>
    <span class="brand-name">Lorena Valdez<br>Foundation</span>
  </div>
  <div class="abs search">Search this Site</div>
  <ul class="abs main-nav">
    <li>About</li>
    <li>Curriculum <svg class="caret" viewBox="0 0 9 6"><path d="M1 1l3.5 3.5L8 1" fill="none" stroke="#b7a5cd" stroke-width="1.3"/></svg></li>
    <li>Admissions <svg class="caret" viewBox="0 0 9 6"><path d="M1 1l3.5 3.5L8 1" fill="none" stroke="#b7a5cd" stroke-width="1.3"/></svg></li>
    <li>News + Events <svg class="caret" viewBox="0 0 9 6"><path d="M1 1l3.5 3.5L8 1" fill="none" stroke="#b7a5cd" stroke-width="1.3"/></svg></li>
    <li>People <svg class="caret" viewBox="0 0 9 6"><path d="M1 1l3.5 3.5L8 1" fill="none" stroke="#b7a5cd" stroke-width="1.3"/></svg></li>
    <li>Contact Us</li>
  </ul>
</header>

<section>
  <div class="abs hero" role="img" aria-label="Smiling student holding books in a stone arcade"></div>
  <h1 class="abs hero-title" style="font-weight:300">Inspiring Fundraising Foundation<br>Website to Provide<br>Academic Scholarships</h1>
</section>

<section>
  <article class="abs feature" style="left:102px">
    <div class="photo" role="img" aria-label="Scholarship application form on a desk" style="background:linear-gradient(160deg,#7a5f4a 0%,#d9d6d0 40%,#eeeeec 100%)"></div>
    <div class="caption"><h3>Student Sholarships Application</h3><p>Lorem ipsum dolor sit amet, consectetuer adipiscing elit.<br>Aenean commodo ligula eget dolor.</p></div>
  </article>
  <article class="abs feature" style="left:436px">
    <div class="photo" role="img" aria-label="Students writing an exam in a classroom" style="background:linear-gradient(160deg,#cfc9c1 0%,#a08777 45%,#6a5a52 100%)"></div>
    <div class="caption"><h3>Student Studying</h3><p>Lorem ipsum dolor sit amet, consectetuer adipiscing elit.<br>Aenean commodo ligula eget dolor.</p></div>
  </article>
  <article class="abs feature" style="left:769px">
    <div class="photo" role="img" aria-label="Two students reading together" style="background:linear-gradient(160deg,#e7e2da 0%,#b9a493 45%,#4c403a 100%)"></div>
    <div class="caption"><h3>Students</h3><p>Lorem ipsum dolor sit amet, consectetuer adipiscing elit.<br>Aenean commodo ligula eget dolor.</p></div>
  </article>
</section>

<section>
  <h2 class="abs intro-title">Aenean imperdiet. Etiam ultricies nisi vel augue Curabitur ullamcorper ultricies.</h2>
  <p class="abs intro-copy">Lorem ipsum dolor sit amet, consectetuer adipiscing elit. Aenean commodo ligula eget dolor. Aenean massa. Cum sociis natoque penatibus et magnis dis parturient montes, nascetur ridiculus mus. Donec quam felis, ultricies nec, pellentesque eu, pretium quis, sem. Nulla consequat massa quis enim. Donec pede justo, fringilla vel, aliquet nec, vulputate eget, arcu. In enim justo, rhoncus ut, imperdiet a, venenatis vitae, justo. Nullam dictum felis eu pede mollis.</p>
  <ul class="abs bullets">
    <li><span class="dot"></span><b>Lorem ipsum</b> dolor sit amet, consectetuer adipiscing elit. Aenean commodo ligula eget</li>
    <li><span class="dot"></span><b>Lorem ipsum</b> dolor sit amet, consectetuer adipiscing elit. Aenean commodo ligula eget</li>
    <li><span class="dot"></span><b>Lorem ipsum</b> dolor sit amet, consectetuer adipiscing elit. Aenean commodo ligula eget</li>
    <li><span class="dot"></span><b>Lorem ipsum</b> dolor sit amet, consectetuer adipiscing elit. Aenean commodo ligula eget</li>
  </ul>
  <div class="abs intro-photo" role="img" aria-label="Graduates in caps and gowns in front of a college building"></div>
</section>

<section>
  <h2 class="abs section-title">Curabitur Tamcorper Atricies.</h2>
  <article class="abs program" style="left:102px">
    <div class="photo" role="img" aria-label="Graduate in cap and gown holding a diploma" style="background:linear-gradient(180deg,#c8c4c0 0%,#7d6f68 50%,#222226 100%)"></div>
    <h4>CONSECTETUER ADIPISCING ELIT</h4>
    <p>Lorem ipsum dolor sit amet, consectetuer<br>adipiscing enean commodo ligula eget.</p>
    <div class="btn">COMMODO LIGULA EGET</div>
  </article>
  <article class="abs program" style="left:439px">
    <div class="photo" role="img" aria-label="Smiling graduates holding diplomas" style="background:linear-gradient(180deg,#b8c29a 0%,#9a8672 45%,#2a2830 100%)"></div>
    <h4>CONSECTETUER ADIPISCING ELIT</h4>
    <p>Lorem ipsum dolor sit amet, consectetuer<br>adipiscing enean commodo ligula eget.</p>
    <div class="btn">COMMODO LIGULA EGET</div>
  </article>
  <article class="abs program" style="left:777px">
    <div class="photo" role="img" aria-label="Graduation caps thrown into a blue sky" style="background:linear-gradient(180deg,#6fa1d6 0%,#9fc2e6 65%,#3a4a6a 100%)"></div>
    <h4>CONSECTETUER ADIPISCING ELIT</h4>
    <p>Lorem ipsum dolor sit amet, consectetuer<br>adipiscing enean commodo ligula eget.</p>
    <div class="btn">COMMODO LIGULA EGET</div>
  </article>
</section>

<section class="abs apply">
  <h2>APPLY NOW</h2>
  <div class="field" style="top:85px"><label><span>*</span>Email Address</label><div class="input"></div></div>
  <div class="field" style="top:151px"><label><span>*</span>First Name</label><div class="input"></div></div>
  <div class="field" style="top:217px"><label><span>*</span>Last Name</label><div class="input"></div></div>
  <div class="field" style="top:283px"><label><span>*</span>How did you hear about us?</label><div class="input"></div></div>
  <div class="field" style="top:349px"><label><span>*</span>Email Lists</label></div>
  <div class="signup">Sign up</div>
</section>

<footer>
  <div class="abs footer"></div>
  <div class="abs footer-brand"><span class="brand-mark"></span><span class="brand-name">Lorena Valdez<br>Foundation</span></div>
  <address class="abs footer-info" style="font-style:normal">
    Lorena Valdez Foundation<br>
    Suite 412 Alder Avenue No 28<br>
    Tel: 00 1555 014 2290 / 00 1555 017 6634<br>
    hello@lorenavaldez.org
  </address>
  <ul class="abs socials" aria-label="Social links">
    <li></li><li></li><li></li><li></li><li></li><li></li>
  </ul>
</footer>
</body>
</html>
```